Web design concept for a IT recruitment agency.

Our website addresses two different target groups:
- Customers (companies) wanting to hire new IT talent
- It talent to find a new JOB

We a looking for a visual design concept that either addresses both target groups in one of the following options:
a. target both groups in 1 single splash page.
b. target both groups in 2 different pages one for both groups
c. or any creative third concept you can come up with

Requirements, we want one overall visual concept, that both target groups can relate to.

Trigger words what we want to express:
- passion / drive
- knowhow
- involvement
- professional/yet playful
- engagement

Background, company culture:
We are a recruitment agency with over 15 years of experience, we have no hard-sale culture.
But we emphasize on long term relationships, showing real interest in people and their needs.

Design requirements:
Use logo
Flat contemporary design

Target Market(s)

Industry/Entity Type

Hire

Number of Pages Required

2 page

Requirements
Must have
• We a looking for a visual design concept that either addresses both target groups

```html
<!DOCTYPE html>
<html lang="en">
<head>
<meta charset="utf-8">
<title>Halvern – IT Recruitment Specialists</title>
<link href="https://fonts.googleapis.com/css2?family=Roboto:wght@300;400;500;700&display=swap" rel="stylesheet">
<style>
:root{
  --blue:#00adef;
  --blue-text:#1a8fcf;
  --nav-blue:#21a9e8;
  --charcoal:#444043;
  --navy:#34405e;
  --grey-icon:#a8a8a8;
  --band:#ececec;
  --white:#fff;
}
*{margin:0;padding:0;box-sizing:border-box}
html,body{width:1200px;height:1200px;overflow:hidden;background:var(--white);font-family:'Roboto',sans-serif}
.page{position:relative;width:1200px;height:1200px;overflow:hidden}
.top-nav{position:absolute;top:16px;left:0;width:1200px;height:40px;background:var(--charcoal)}
.top-nav a{position:absolute;top:13px;font-size:11.5px;font-weight:700;color:var(--nav-blue);text-decoration:none}
.logo-notch{position:absolute;left:560px;top:13px;width:96px;height:96px;border-radius:50%;background:var(--white)}
.brand{position:absolute;left:0;width:1200px;top:74px;text-align:center;font-size:38px;font-weight:400;color:#2b2b2b;letter-spacing:.5px}
.brand-dot{position:absolute;left:590px;top:30px;width:36px;height:36px;border-radius:50%;background:var(--blue)}
.social{position:absolute;top:99px;width:11px;height:11px;border-radius:50%;background:var(--grey-icon)}
.call{position:absolute;left:900px;top:92px;display:flex;align-items:center;gap:8px;font-size:17.5px;color:var(--navy)}
.call b{font-weight:400;color:var(--blue)}
.hero{position:absolute;left:56px;top:152px;width:1088px;height:336px;overflow:hidden}
.hero svg{position:absolute;inset:0}
.hero h1{position:absolute;left:76px;top:96px;font-size:46px;font-weight:300;color:var(--white);letter-spacing:.3px}
.hero h2{position:absolute;left:76px;top:153px;font-size:27px;font-weight:700;color:var(--white)}
.btn{position:absolute;display:flex;align-items:center;justify-content:space-between;border-radius:4px;color:var(--white);font-weight:400}
.btn svg{position:static}
.btn-dark{background:var(--charcoal)}
.btn-blue{background:var(--blue)}
.hero .btn{left:78px;top:214px;width:304px;height:48px;padding:0 22px 0 24px;font-size:14.5px}
.intro{position:absolute;left:150px;top:538px;width:900px;text-align:center;font-size:17px;line-height:27px;color:var(--blue-text)}
.card{position:absolute;top:664px;height:272px;overflow:hidden;color:var(--white)}
.card svg.bg{position:absolute;inset:0}
.card .icon{position:absolute;left:36px;top:22px}
.card h3{position:absolute;left:36px;top:62px;font-size:29px;font-weight:300}
.card p{position:absolute;left:36px;top:102px;width:210px;font-size:13px;line-height:23px}
.card .btn{left:38px;top:192px;width:160px;height:40px;padding:0 20px;font-size:13.5px}
.employers{left:136px;width:464px;background:var(--charcoal)}
.candidates{left:602px;width:467px;background:var(--blue)}
.candidates .icon,.candidates h3,.candidates p,.candidates .btn{left:42px}
.expertise-title{position:absolute;left:0;width:1200px;top:974px;text-align:center;font-size:26px;font-weight:300;color:var(--navy)}
.expertise{position:absolute;top:1020px;list-style:none}
.expertise li{display:flex;align-items:center;gap:7px;height:23px;font-size:13px;color:var(--navy)}
.lower-band{position:absolute;left:0;top:1128px;width:1200px;height:72px;background:var(--band)}
.lower-band h4{position:absolute;top:44px;font-size:26px;font-weight:300;color:var(--navy)}
</style>
</head>
<body>
<svg width="0" height="0" style="position:absolute">
  <defs>
    <symbol id="arrow" viewBox="0 0 24 20"><path d="M14 1 L23 9 L14 17 V12 C8 12 4 14 1 19 C2 11 6 6 14 6 Z" fill="currentColor"/></symbol>
  </defs>
</svg>
<div class="page">
  <nav class="top-nav">
    <a style="left:133px">Home</a>
    <a style="left:262px">About Us</a>
    <a style="left:411px">What we do</a>
    <a style="left:709px">Employers</a>
    <a style="left:853px">Candidates</a>
    <a style="left:1001px">Contact Us</a>
  </nav>
  <div class="logo-notch"></div>
  <div class="brand-dot"></div>
  <div class="brand">Halvern</div>

  <span class="social" style="left:130px"></span>
  <span class="social" style="left:165px"></span>
  <span class="social" style="left:204px"></span>

  <div class="call">
    <svg width="28" height="28" viewBox="0 0 28 28"><circle cx="14" cy="14" r="12.5" fill="none" stroke="#c9c9c9" stroke-width="1.5"/><path d="M9 8 C8 12 12 19 18 20 L20 17 L17 15 L15.5 16.5 C13.5 15.5 12 14 11.5 12 L13 10.5 L11 7.5 Z" fill="#c9c9c9"/></svg>
    <span><b>Call</b> 01 555 0199</span>
  </div>

  <section class="hero">
    <svg width="1088" height="336" viewBox="0 0 1088 336">
      <defs><linearGradient id="heroPhoto" x1="0" x2="1"><stop offset="0" stop-color="#d9d9db"/><stop offset="1" stop-color="#eeeeef"/></linearGradient></defs>
      <rect role="img" aria-label="Photo of a smiling team of five recruitment consultants in business attire" x="420" y="0" width="668" height="336" fill="url(#heroPhoto)"/>
      <path d="M0 0 H528 C610 90 630 240 496 336 H0 Z" fill="var(--blue)"/>
      <path d="M468 0 H500 C580 100 570 250 470 336 C545 250 550 110 468 0 Z" fill="#e8e8ea"/>
    </svg>
    <h1>Welcome to Halvern</h1>
    <h2>IT Recruitment Specialists</h2>
    <a class="btn btn-dark">Find out more about what we do <svg width="24" height="20"><use href="#arrow" color="#fff"/></svg></a>
  </section>

  <p class="intro">Lorem ipsum dolor sit amet, consectetur adipiscing elit, sed do eiusmod tempor incididunt ut labore et dolore magna aliqua enim ad minim veniam, quis nostrud exercitation ullamco laboris nisi ut aliquip ex ea commodo consequat aute irure dolor in reprehenderit in voluptate velit esse cillum dolore eu fugiat.</p>

  <article class="card employers">
    <svg class="bg" width="464" height="272" viewBox="0 0 464 272">
      <rect role="img" aria-label="Photo of a man in a blue shirt working on a laptop" x="220" y="0" width="244" height="272" fill="#8a8fa0"/>
      <path d="M0 0 H210 C300 80 300 200 220 272 H0 Z" fill="#3b3739"/>
      <path d="M0 0 H200 C275 80 275 200 200 272 H0 Z" fill="var(--charcoal)"/>
    </svg>
    <svg class="icon" width="28" height="30" viewBox="0 0 28 30"><circle cx="14" cy="8" r="7" fill="var(--blue)"/><path d="M1 30 V24 C1 19 6 17 14 17 C22 17 27 19 27 24 V30 Z" fill="var(--blue)"/></svg>
    <h3>Employers</h3>
    <p>Lorem ipsum dolor sit amet odio consectetur adipiscing eiusmod incididunt dolore.</p>
    <a class="btn btn-blue">Find out more <svg width="20" height="17"><use href="#arrow" color="#fff"/></svg></a>
  </article>

  <article class="card candidates">
    <svg class="bg" width="467" height="272" viewBox="0 0 467 272">
      <rect role="img" aria-label="Photo of a young woman on the phone at a laptop in a green office" x="230" y="0" width="237" height="272" fill="#b9b3a4"/>
      <path d="M0 0 H240 C330 80 330 200 230 272 H0 Z" fill="#1f93cf"/>
      <path d="M0 0 H220 C300 80 300 200 205 272 H0 Z" fill="var(--blue)"/>
    </svg>
    <svg class="icon" width="40" height="30" viewBox="0 0 40 30"><circle cx="12" cy="8" r="7" fill="var(--charcoal)"/><path d="M0 30 V24 C0 19 5 17 12 17 C19 17 24 19 24 24 V30 Z" fill="var(--charcoal)"/><circle cx="30" cy="12" r="5.5" fill="var(--charcoal)"/><path d="M22 30 V26 C22 22 26 20 31 20 C36 20 40 22 40 26 V30 Z" fill="var(--charcoal)"/></svg>
    <h3>Candidates</h3>
    <p>Enim ad minim veniam quis nostrud laboris nisi ut aliquip commodo adipiscing elit.</p>
    <a class="btn btn-dark">Find out more <svg width="20" height="17"><use href="#arrow" color="#fff"/></svg></a>
  </article>

  <h3 class="expertise-title">We offer specialist recruitment knowledge and experience in ...</h3>
  <ul class="expertise" style="left:268px">
    <li><svg width="12" height="10"><use href="#arrow" color="var(--blue)"/></svg>Lorem ipsum dolor consectetur</li>
    <li><svg width="12" height="10"><use href="#arrow" color="var(--blue)"/></svg>Adipiscing elit sed eiusmod</li>
    <li><svg width="12" height="10"><use href="#arrow" color="var(--blue)"/></svg>Tempor incididunt labore</li>
  </ul>
  <ul class="expertise" style="left:508px">
    <li><svg width="12" height="10"><use href="#arrow" color="var(--blue)"/></svg>Duisaute reprehenderit</li>
    <li><svg width="12" height="10"><use href="#arrow" color="var(--blue)"/></svg>Voluptate velit esse cillum</li>
    <li><svg width="12" height="10"><use href="#arrow" color="var(--blue)"/></svg>Excepteur sint occaecat</li>
  </ul>
  <ul class="expertise" style="left:724px">
    <li><svg width="12" height="10"><use href="#arrow" color="var(--blue)"/></svg>Dolore magna aliquat enim</li>
    <li><svg width="12" height="10"><use href="#arrow" color="var(--blue)"/></svg>Veniam quis nostrud exercitation</li>
    <li><svg width="12" height="10"><use href="#arrow" color="var(--blue)"/></svg>Ullamco laboris</li>
  </ul>

  <section class="lower-band">
    <h4 style="left:133px">What our clients think</h4>
    <h4 style="left:612px">Latest Vacancies</h4>
  </section>
</div>
</body>
</html>
```